BRQ-Bluefield Ridge Quorum LLC (Business Cards)

The attached design was selected as the logo for our company. I need to proceed on creating our business cards.

Teodoro

Target Market(s)

This is a technology and Project Management company. The audience will be business decision makers of a diversity of companies.

Industry/Entity Type

Business

Font styles to use
Sans Serif
Script

Colors

Designer to choose colors to be used in the design.

```html
<!DOCTYPE html>
<html lang="en">
<head>
<meta charset="utf-8">
<title>BRQ-Bluefield Ridge Quorum LLC — Business Cards</title>
<link rel="stylesheet" href="https://fonts.googleapis.com/css2?family=Open+Sans:wght@400;600;700&display=swap">
<style>
  :root {
    --stage: #e9e9ee;
    --card: #ffffff;
    --brand-red: #9e1b21;
    --ink: #2b2b2b;
    --ink-soft: #555555;
    --divider: #8a8a8a;
  }
  * { box-sizing: border-box; margin: 0; padding: 0; }
  html, body { width: 1200px; height: 911px; overflow: hidden; }
  body {
    background: var(--stage);
    font-family: "Open Sans", Arial, sans-serif;
    color: var(--ink);
    position: relative;
  }
  .card {
    position: absolute;
    left: 290px;
    width: 620px;
    height: 354px;
    background: var(--card);
    border-radius: 22px;
    box-shadow: 0 6px 18px rgba(0,0,0,0.12);
    overflow: hidden;
  }
  .card--front { top: 70px; }
  .card--back { top: 484px; }

  .rule {
    position: absolute;
    left: 0; right: 0;
    height: 4px;
    background: var(--brand-red);
  }
  .rule__marker {
    position: absolute;
    top: -8px;
    width: 20px; height: 20px;
    background: var(--brand-red);
  }

  .company-name {
    position: absolute;
    font-weight: 400;
    color: var(--ink);
    white-space: nowrap;
    line-height: 1.2;
  }

  /* Front */
  .card--front .company-name {
    left: 0; right: 0;
    top: 132px;
    text-align: center;
    font-size: 26px;
    letter-spacing: 0.5px;
  }
  .card--front .rule { top: 218px; }
  .card--front .rule__marker { left: 300px; }

  /* Back */
  .card--back .company-name {
    left: 40px; top: 46px;
    font-size: 20px;
    letter-spacing: 0.3px;
  }
  .card--back .rule { top: 262px; }
  .card--back .rule__marker { left: 250px; }

  .address {
    position: absolute;
    left: 40px; top: 290px;
    font-size: 17px;
    color: var(--ink);
  }

  .contact {
    position: absolute;
    left: 360px; top: 108px;
    border-left: 2px solid var(--divider);
    padding-left: 18px;
  }
  .contact__name {
    font-size: 19px;
    font-weight: 700;
    letter-spacing: 0.5px;
    text-transform: uppercase;
    white-space: nowrap;
  }
  .contact__title {
    font-size: 15px;
    color: var(--ink-soft);
    margin-bottom: 12px;
  }
  .contact__list { list-style: none; }
  .contact__item {
    display: flex;
    align-items: center;
    gap: 10px;
    font-size: 13px;
    color: var(--ink);
    line-height: 22px;
    white-space: nowrap;
  }
  .contact__bullet {
    width: 10px; height: 10px;
    background: var(--brand-red);
    flex: none;
  }
</style>
</head>
<body>
  <section class="card card--front" aria-label="Business card front">
    <p class="company-name">Bluefield Ridge Quorum</p>
    <div class="rule"><span class="rule__marker"></span></div>
  </section>

  <section class="card card--back" aria-label="Business card back">
    <p class="company-name">Bluefield Ridge Quorum</p>
    <div class="contact">
      <p class="contact__name">Marcus Delaney</p>
      <p class="contact__title">Managing Director</p>
      <ul class="contact__list">
        <li class="contact__item"><span class="contact__bullet"></span>012 555 0147</li>
        <li class="contact__item"><span class="contact__bullet"></span>012 555 0148</li>
        <li class="contact__item"><span class="contact__bullet"></span>mail@bluefieldridge.com</li>
        <li class="contact__item"><span class="contact__bullet"></span>bluefieldridge.com</li>
      </ul>
    </div>
    <div class="rule"><span class="rule__marker"></span></div>
    <p class="address">Northgate, Suite 024, Alder St. Ravena</p>
  </section>
</body>
</html>
```